Design a Logo and Stationary for 'Plan Ledger Pro'

Design a logo and stationary for a CAD drafting company called "Plan Ledger Pro".
The company specialises in producing CAD drawings for the construction industry post completion, typically marking up plans to reflect changes which have occurred during the construction process. We are looking for a logo that is professional in appearance and perhaps incorporates a picture relating to construction or drafting. The logo should be original and clever.
The logo should be suitable for use in colour and black and white and for printing on white paper.
The company are looking for at least a logo, letterhead, business card and invoice in both colour and black and white. The logo will be used on a website and for other marketing materials.
Please make contact if you require further information or have enquiries.

```html
<!DOCTYPE html>
<html lang="en">
<head>
<meta charset="utf-8">
<title>Plan Ledger Pro – Stationery</title>
<link href="https://fonts.googleapis.com/css2?family=Arimo:wght@400;700&display=swap" rel="stylesheet">
<style>
  :root {
    --board-top: #a3a4a6;
    --board-bottom: #77787a;
    --paper: #ffffff;
    --ink: #8a8c8f;
    --ink-strong: #6e7073;
    --ghost: #f1f1f2;
    --flap: #f6f6f6;
    --shadow: rgba(0,0,0,0.22);
  }
  * { box-sizing: border-box; margin: 0; padding: 0; }
  html, body { width: 1200px; height: 900px; overflow: hidden; }
  body {
    font-family: "Arimo", Arial, sans-serif;
    color: var(--ink);
    background: linear-gradient(180deg, var(--board-top), var(--board-bottom));
    position: relative;
  }
  .sheet {
    position: absolute;
    background: var(--paper);
    overflow: hidden;
    box-shadow: 0 2px 5px var(--shadow);
  }
  .brand {
    position: absolute;
    display: flex;
    align-items: center;
    gap: 10px;
    color: var(--ink);
    font-weight: 400;
    white-space: nowrap;
  }
  .brand-square { background: var(--ink); flex: none; }
  .ghost-letter {
    position: absolute;
    color: var(--ghost);
    font-weight: 700;
    line-height: 1;
    pointer-events: none;
  }

  /* Letterhead */
  .letterhead { left: 56px; top: 80px; width: 531px; height: 731px; }
  .letterhead .brand { left: 56px; top: 38px; font-size: 24px; }
  .letterhead .brand-square { width: 34px; height: 34px; }
  .letterhead .ghost-letter { left: -24px; top: 520px; font-size: 520px; }
  .letterhead .contact {
    position: absolute; left: 387px; top: 637px;
    font-size: 9px; line-height: 11px;
  }
  .contact .gap { margin-top: 7px; }
  .contact .web { font-weight: 700; color: var(--ink-strong); }

  /* Business cards */
  .card-front { left: 617px; top: 84px; width: 228px; height: 125px; }
  .card-front .brand { left: 22px; top: 13px; font-size: 11px; gap: 5px; }
  .card-front .brand-square { width: 14px; height: 14px; }
  .card-front .ghost-letter { left: -6px; top: 40px; font-size: 190px; }
  .card-front .person {
    position: absolute; left: 145px; top: 51px;
    font-size: 5px; line-height: 6.5px;
  }
  .person .name { font-size: 11px; line-height: 13px; font-weight: 700; color: var(--ink-strong); margin-bottom: 2px; }
  .person .gap { margin-top: 4px; }
  .person .web { font-weight: 700; color: var(--ink-strong); }

  .card-back { left: 865px; top: 84px; width: 227px; height: 125px; }
  .card-back .brand {
    left: 0; right: 0; top: 44px;
    flex-direction: column; gap: 6px; font-size: 10px;
  }
  .card-back .brand-square { width: 22px; height: 22px; }

  /* Envelope */
  .envelope { left: 611px; top: 231px; width: 529px; height: 277px; }
  .envelope .flap { position: absolute; left: 0; top: 0; }
  .envelope .ghost-letter { left: -10px; top: 120px; font-size: 360px; }
  .envelope .brand {
    right: 56px; top: 156px;
    flex-direction: column; align-items: center; gap: 8px; font-size: 13px;
  }
  .envelope .brand-square { width: 30px; height: 30px; }
</style>
</head>
<body>

<section class="sheet letterhead" aria-label="Letterhead">
  <div class="ghost-letter" aria-hidden="true">p</div>
  <div class="brand"><span class="brand-square"></span>Plan Ledger Pro</div>
  <address class="contact" style="font-style:normal">
    <div>Street Address</div>
    <div>PO Box 40517</div>
    <div>Renton, WA 98057-0517</div>
    <div class="gap">(425) 555-0193</div>
    <div>planledgerpro@email.com</div>
    <div class="web">www.planledgerpro.com</div>
  </address>
</section>

<section class="sheet card-front" aria-label="Business card front">
  <div class="ghost-letter" aria-hidden="true">p</div>
  <div class="brand"><span class="brand-square"></span>Plan Ledger Pro</div>
  <address class="person" style="font-style:normal">
    <div class="name">Mara Ellison</div>
    <div>Street Address</div>
    <div>PO Box 40517</div>
    <div>Renton, WA 98057-0517</div>
    <div class="gap">(425) 555-0193</div>
    <div>planledgerpro@email.com</div>
    <div class="web">www.planledgerpro.com</div>
  </address>
</section>

<section class="sheet card-back" aria-label="Business card back">
  <div class="brand"><span class="brand-square"></span>Plan Ledger Pro</div>
</section>

<section class="sheet envelope" aria-label="Envelope">
  <div class="ghost-letter" aria-hidden="true">p</div>
  <svg class="flap" width="529" height="80" viewBox="0 0 529 80" aria-hidden="true">
    <polygon points="0,0 529,0 505,73 26,73" fill="var(--flap)"/>
    <polyline points="0,0 26,73 505,73 529,0" fill="none" stroke="#d9d9da" stroke-width="1"/>
    <line x1="26" y1="75" x2="505" y2="75" stroke="#ececec" stroke-width="2"/>
  </svg>
  <div class="brand"><span class="brand-square"></span>Plan Ledger Pro</div>
</section>

</body>
</html>
```